Copperline Real Estate Company needs Website

I need an updated, easy to use website for my Real Estate company based out of Amarillo, TX.
Our current focus is on residential rental properties. However we are looking to expand into multi-family rentals, commercial rentals, and vacation rentals.
We also offer Real Estate Listing services.
The final design should be user friendly.

Target Market(s)

Homeowners and renters

Industry/Entity Type

Real Estate

Coding

Coded - Design and coding required

Number of Pages Required

1 page

Font styles to use
Sans Serif

Requirements
Must have
• Easy to navigate

```html
<!DOCTYPE html>
<html lang="en">
<head>
<meta charset="utf-8">
<title>Copperline Properties</title>
<link rel="stylesheet" href="https://fonts.googleapis.com/css2?family=Lato:wght@300;400;700&family=Montserrat:wght@200;300;400;600;700&display=swap">
<style>
:root{
  --blue:#1e9fdc;
  --blue-dark:#1686bd;
  --orange:#f0890e;
  --ink:#2b2b2b;
  --text:#555;
  --muted:#8a8a8a;
  --line:#e2e2e2;
  --grey-bg:#f4f4f4;
  --footer:#353535;
  --white:#fff;
}
*{box-sizing:border-box;margin:0;padding:0}
html,body{width:1200px;height:2459px;overflow:hidden}
body{font-family:'Lato',sans-serif;color:var(--text);background:var(--white);position:relative}
a{text-decoration:none;color:inherit}
h1,h2,h3{font-weight:inherit}

/* header */
.site-header{height:79px;display:flex;align-items:center;padding:0 156px;background:var(--white)}
.brand{display:flex;align-items:center;gap:8px;font-family:'Montserrat',sans-serif;font-weight:700;font-size:26px;color:var(--blue-dark);width:246px}
.brand-dot{width:14px;height:14px;border-radius:50%;background:var(--blue)}
.main-nav{display:flex;gap:26px;font-family:'Montserrat',sans-serif;font-size:13px;color:#444;height:79px;align-items:center}
.main-nav a{height:79px;display:flex;align-items:center;border-top:2px solid transparent}
.main-nav a.active{color:var(--blue);border-top-color:var(--blue)}
.caret{font-size:9px;margin-left:6px}
.header-phone{margin-left:auto;display:flex;align-items:center;gap:10px;font-family:'Montserrat',sans-serif;font-size:17px;color:#333}

/* hero */
.hero{height:401px;position:relative;background:linear-gradient(180deg,#3c4757 0%,#5b5a55 45%,#3a3a32 80%,#25281f 100%);text-align:center;color:var(--white)}
.hero-title{position:absolute;top:160px;left:0;right:0;font-family:'Montserrat',sans-serif;font-weight:300;font-size:38px;line-height:44px;letter-spacing:1px}
.hero-sub{position:absolute;top:208px;left:0;right:0;font-family:'Montserrat',sans-serif;font-weight:300;font-size:22px;line-height:28px}
.hero-arrow{position:absolute;top:181px}
.hero-arrow.prev{left:90px}.hero-arrow.next{left:1068px}

/* search band */
.search-band{height:244px;background:linear-gradient(180deg,#2aa3df,#1e9ad8);text-align:center;color:var(--white);position:relative}
.search-title{padding-top:61px;font-family:'Montserrat',sans-serif;font-weight:600;font-size:20px}
.search-sub{margin-top:6px;font-size:15px}
.search-form{position:absolute;left:284px;top:126px;width:631px;height:54px;background:rgba(255,255,255,.3);padding:10px 11px;display:flex}
.field{background:var(--white);color:#777;font-size:12px;display:flex;align-items:center;justify-content:space-between;padding:0 12px;height:34px}
.field.type{width:206px;border-right:1px solid var(--line)}
.field.zip{width:296px;justify-content:flex-start;gap:6px}
.field.zip .caret{margin-left:auto}
.search-btn{width:107px;height:34px;background:var(--orange);color:var(--white);font-family:'Montserrat',sans-serif;font-size:11px;font-weight:600;letter-spacing:1px;display:flex;align-items:center;justify-content:center;gap:6px}

/* listings */
.listings{height:939px;background:var(--grey-bg);position:relative;text-align:center}
.section-title{padding-top:78px;font-family:'Montserrat',sans-serif;font-weight:400;font-size:29px;color:var(--ink)}
.section-sub{margin-top:8px;font-size:14px;color:#666}
.tabs{display:flex;justify-content:center;gap:7px;margin-top:22px}
.tab{height:28px;border:1px solid #bbb;background:var(--white);font-family:'Montserrat',sans-serif;font-size:11px;letter-spacing:1px;color:#444;display:flex;align-items:center;justify-content:center;position:relative}
.tab.active{background:var(--blue);border-color:var(--blue);color:var(--white);font-weight:600}
.tab.active::after{content:"";position:absolute;bottom:-7px;left:50%;margin-left:-6px;border:6px solid transparent;border-top-color:var(--blue);border-bottom:0}
.cards{position:absolute;left:156px;top:227px;width:888px;display:grid;grid-template-columns:repeat(4,205px);column-gap:22px;row-gap:25px;text-align:left}
.card{background:var(--white);height:280px;overflow:hidden}
.card.hover{box-shadow:0 4px 12px rgba(0,0,0,.12)}
.card-media{height:143px;position:relative}
.media-pool{background:linear-gradient(180deg,#a9c6de 0%,#e8dfcd 45%,#4f6d86 100%)}
.media-tower{background:linear-gradient(180deg,#2c5a74 0%,#b9c3c7 55%,#3d5e70 100%)}
.media-house{background:linear-gradient(180deg,#9c8ccc 0%,#6a5f8d 50%,#2d3a25 100%)}
.card-tag{position:absolute;left:0;right:0;bottom:0;height:26px;background:rgba(22,52,74,.75);color:var(--white);font-family:'Montserrat',sans-serif;font-size:11px;font-weight:600;line-height:26px;padding:0 15px}
.card-body{padding:14px 15px}
.card-body p,.card-body h3{white-space:nowrap}
.card-name{font-family:'Montserrat',sans-serif;font-weight:400;font-size:14px;line-height:18px;color:#333}
.card-state{font-size:12px;line-height:14px;color:#777;margin-top:2px}
.card-price{margin-top:16px;font-size:11px;line-height:16px;color:#999;padding-bottom:12px;border-bottom:1px solid var(--line)}
.card-price b{color:var(--orange);font-weight:400;font-size:12px;margin-right:8px}
.card-specs{margin-top:14px;font-size:11px;line-height:14px;color:#444}
.card-link{margin-top:14px;font-size:12px;line-height:14px;color:var(--blue);font-family:'Montserrat',sans-serif}
.btn{display:inline-flex;align-items:center;justify-content:center;background:var(--blue);color:var(--white);font-family:'Montserrat',sans-serif;font-size:11px;font-weight:600;letter-spacing:1px;border-bottom:2px solid var(--blue-dark)}
.view-all{position:absolute;left:513px;top:847px;width:174px;height:31px}

/* process */
.process{height:700px;position:relative;text-align:center}
.process-title{padding-top:59px;font-family:'Montserrat',sans-serif;font-weight:600;font-size:20px;color:var(--ink)}
.steps{position:absolute;top:119px;left:145px;width:910px;display:flex;justify-content:space-between}
.step{width:304px}
.step-name{margin-top:18px;font-family:'Montserrat',sans-serif;font-weight:600;font-size:14px;color:#333}
.step-text{margin:14px auto 0;width:262px;font-size:12px;line-height:17px;color:#888}
.step-more{margin-top:22px;font-size:12px;color:#666}
.step-more.hot{color:var(--blue)}
.step-arrow{position:absolute;top:46px}
.divider{position:absolute;top:461px;left:156px;width:888px;height:1px;background:var(--line)}
.divider-knob{position:absolute;left:426px;top:-18px;width:36px;height:36px;border-radius:50%;border:1px solid #ccc;background:var(--white);display:flex;align-items:center;justify-content:center}
.cta-title{position:absolute;top:518px;left:0;right:0;font-family:'Lato',sans-serif;font-weight:300;font-size:30px;color:#444}
.cta-sub{position:absolute;top:556px;left:0;right:0;font-family:'Montserrat',sans-serif;font-size:18px;color:#222}
.cta-btn{position:absolute;left:544px;top:604px;width:112px;height:31px}

/* footer */
.site-footer{position:absolute;left:0;right:0;top:2363px;height:96px;background:var(--footer);padding:26px 156px;color:#ddd;font-size:12px}
.footer-links{display:flex;gap:9px}
.footer-links .sep{color:#999}
.footer-links .hot{color:var(--blue)}
.copyright{margin-top:6px;font-size:13px}
.socials{position:absolute;right:169px;top:38px;display:flex;gap:6px}
.socials span{width:21px;height:21px;border-radius:50%;background:#8a8a8a}
.socials span.hot{background:var(--blue)}
</style>
</head>
<body>

<header class="site-header">
  <div class="brand"><span class="brand-dot"></span>Copperline</div>
  <nav class="main-nav">
    <a class="active" href="#">Home</a>
    <a href="#">Real Estate</a>
    <a href="#">Rental Properties<span class="caret">&#9660;</span></a>
    <a href="#">Services</a>
    <a href="#">Contact Us</a>
  </nav>
  <div class="header-phone">
    <svg width="18" height="22" viewBox="0 0 18 22"><rect x="2" y="1" width="14" height="20" rx="2" fill="none" stroke="#f0890e" stroke-width="2.5"/><rect x="6" y="16" width="6" height="2" fill="#f0890e"/></svg>
    01 2345 6789
  </div>
</header>

<section class="hero" role="img" aria-label="Photo of a modern timber house with a pool at dusk">
  <h1 class="hero-title">ONE STOP SOLUTION</h1>
  <p class="hero-sub">for All Rental Properties!</p>
  <svg class="hero-arrow prev" width="40" height="40" viewBox="0 0 40 40"><rect x="8" y="8" width="24" height="24" transform="rotate(45 20 20)" fill="none" stroke="#fff" stroke-width="2"/><path d="M23 14l-6 6 6 6" fill="none" stroke="#fff" stroke-width="2"/></svg>
  <svg class="hero-arrow next" width="40" height="40" viewBox="0 0 40 40"><rect x="8" y="8" width="24" height="24" transform="rotate(45 20 20)" fill="#fff"/><path d="M17 14l6 6-6 6" fill="none" stroke="#1e9fdc" stroke-width="2.5"/></svg>
</section>

<section class="search-band" role="img" aria-label="Faint map of the southern United States behind the search panel">
  <h2 class="search-title">Discover Your Perfect Rental Property</h2>
  <p class="search-sub">Real Estate company based out of Amarillo, TX.</p>
  <form class="search-form">
    <div class="field type">Rental Properties Type<span class="caret">&#9660;</span></div>
    <div class="field zip">
      <svg width="10" height="13" viewBox="0 0 10 13"><path d="M5 0a5 5 0 0 0-5 5c0 4 5 8 5 8s5-4 5-8a5 5 0 0 0-5-5z" fill="#999"/><circle cx="5" cy="5" r="1.8" fill="#fff"/></svg>
      Enter city zip code<span class="caret">&#9660;</span>
    </div>
    <div class="search-btn">
      <svg width="11" height="11" viewBox="0 0 11 11"><circle cx="4.5" cy="4.5" r="3.3" fill="none" stroke="#fff" stroke-width="1.6"/><path d="M7 7l3 3" stroke="#fff" stroke-width="1.8"/></svg>
      SEARCH
    </div>
  </form>
</section>

<section class="listings">
  <h2 class="section-title">Rental Properties</h2>
  <p class="section-sub">See our recent listing here, you will find all kinds of properties.</p>
  <div class="tabs">
    <span class="tab active" style="width:122px">RESIDENTIAL</span>
    <span class="tab" style="width:121px">COMMERCIAL</span>
    <span class="tab" style="width:121px">MULTI-FAMILY</span>
    <span class="tab" style="width:118px">VACATION</span>
  </div>

  <div class="cards">
    <article class="card">
      <div class="card-media media-pool" role="img" aria-label="Photo of a modern apartment with pool"><span class="card-tag">Apartment</span></div>
      <div class="card-body"><h3 class="card-name">Ridge High Line 89-916</h3><p class="card-state">(Arizona)</p>
        <p class="card-price"><b>Price: $5,876.00</b>/ Per Month</p><p class="card-specs">2500Sq ft &nbsp;/&nbsp; 4 Bedroom &nbsp;/&nbsp; 3 Bath</p></div>
    </article>
    <article class="card hover">
      <div class="card-media media-tower" role="img" aria-label="Photo of a multi-storey residential building"><span class="card-tag">Villa</span></div>
      <div class="card-body"><h3 class="card-name">Maple Morningside</h3><p class="card-state">(Michigan)</p>
        <p class="card-price"><b>Price: $5,876.00</b>/ Per Month</p><p class="card-link">View Detail &rarr;</p></div>
    </article>
    <article class="card">
      <div class="card-media media-house" role="img" aria-label="Photo of a large family house at dusk"><span class="card-tag">Family Home</span></div>
      <div class="card-body"><h3 class="card-name">Prism at Park Row</h3><p class="card-state">(South Dakota)</p>
        <p class="card-price"><b>Price: $5,876.00</b>/ Per Month</p><p class="card-specs">2500Sq ft &nbsp;/&nbsp; 4 Bedroom &nbsp;/&nbsp; 3 Bath</p></div>
    </article>
    <article class="card">
      <div class="card-media media-pool" role="img" aria-label="Photo of a modern apartment with pool"><span class="card-tag">Apartment</span></div>
      <div class="card-body"><h3 class="card-name">Ridge High Line 89-916</h3><p class="card-state">(Arizona)</p>
        <p class="card-price"><b>Price: $5,876.00</b>/ Per Month</p><p class="card-specs">2500Sq ft &nbsp;/&nbsp; 4 Bedroom &nbsp;/&nbsp; 3 Bath</p></div>
    </article>

    <article class="card">
      <div class="card-media media-pool" role="img" aria-label="Photo of a modern apartment with pool"><span class="card-tag">Apartment</span></div>
      <div class="card-body"><h3 class="card-name">Ridge High Line 89-916</h3><p class="card-state">(Arizona)</p>
        <p class="card-price"><b>Price: $5,876.00</b>/ Per Month</p><p class="card-specs">2500Sq ft &nbsp;/&nbsp; 4 Bedroom &nbsp;/&nbsp; 3 Bath</p></div>
    </article>
    <article class="card">
      <div class="card-media media-tower" role="img" aria-label="Photo of a multi-storey residential building"><span class="card-tag">Villa</span></div>
      <div class="card-body"><h3 class="card-name">Maple Morningside</h3><p class="card-state">(Michigan)</p>
        <p class="card-price"><b>Price: $5,876.00</b>/ Per Month</p><p class="card-specs">2500Sq ft &nbsp;/&nbsp; 4 Bedroom &nbsp;/&nbsp; 3 Bath</p></div>
    </article>
    <article class="card">
      <div class="card-media media-house" role="img" aria-label="Photo of a large family house at dusk"><span class="card-tag">Family Home</span></div>
      <div class="card-body"><h3 class="card-name">Prism at Park Row</h3><p class="card-state">(South Dakota)</p>
        <p class="card-price"><b>Price: $5,876.00</b>/ Per Month</p><p class="card-specs">2500Sq ft &nbsp;/&nbsp; 4 Bedroom &nbsp;/&nbsp; 3 Bath</p></div>
    </article>
    <article class="card">
      <div class="card-media media-pool" role="img" aria-label="Photo of a modern apartment with pool"><span class="card-tag">Apartment</span></div>
      <div class="card-body"><h3 class="card-name">Ridge High Line 89-916</h3><p class="card-state">(Arizona)</p>
        <p class="card-price"><b>Price: $5,876.00</b>/ Per Month</p><p class="card-specs">2500Sq ft &nbsp;/&nbsp; 4 Bedroom &nbsp;/&nbsp; 3 Bath</p></div>
    </article>
  </div>

  <a class="btn view-all" href="#">VIEW ALL PROPERTY</a>
</section>

<section class="process">
  <h2 class="process-title">We Make Your Life Easy. Here's How.</h2>
  <div class="steps">
    <div class="step">
      <svg width="130" height="150" viewBox="0 0 130 150"><path d="M65 2a63 63 0 0 1 12 124.8L65 140l-12-13.2A63 63 0 0 1 65 2z" fill="#fff" stroke="#ccc" stroke-width="1.5"/>
        <rect x="52" y="46" width="26" height="32" rx="2" fill="#f0890e"/><path d="M57 54h16M57 60h16M57 66h16M57 72h10" stroke="#fff" stroke-width="2"/></svg>
      <h3 class="step-name">Hotest Listing</h3>
      <p class="step-text">Lorem Ipsum has been the industry's standard dummy text ever since the 1500s, when an unknown printer took a galley of type</p>
      <p class="step-more">Read More &rarr;</p>
    </div>
    <div class="step">
      <svg width="130" height="150" viewBox="0 0 130 150"><path d="M65 2a63 63 0 0 1 12 124.8L65 140l-12-13.2A63 63 0 0 1 65 2z" fill="#f0890e"/>
        <circle cx="65" cy="56" r="7" fill="#fff"/><circle cx="51" cy="60" r="5.5" fill="#fff"/><circle cx="79" cy="60" r="5.5" fill="#fff"/>
        <path d="M53 78a12 12 0 0 1 24 0zM40 78a10 10 0 0 1 15-9v9zM90 78a10 10 0 0 0-15-9v9z" fill="#fff"/></svg>
      <h3 class="step-name">Knowledgeable Agents</h3>
      <p class="step-text">Lorem Ipsum has been the industry's standard dummy text ever since the 1500s, when an unknown printer took a galley of type</p>
      <p class="step-more hot">Read More &rarr;</p>
    </div>
    <div class="step">
      <svg width="130" height="150" viewBox="0 0 130 150"><path d="M65 2a63 63 0 0 1 12 124.8L65 140l-12-13.2A63 63 0 0 1 65 2z" fill="#fff" stroke="#ccc" stroke-width="1.5"/>
        <circle cx="65" cy="64" r="19" fill="#f0890e"/><path d="M73 56l-5 12-11 4 5-12z" fill="#fff"/></svg>
      <h3 class="step-name">Expertise and Guidance</h3>
      <p class="step-text">Lorem Ipsum has been the industry's standard dummy text ever since the 1500s, when an unknown printer took a galley of type</p>
      <p class="step-more">Read More &rarr;</p>
    </div>
    <svg class="step-arrow" style="left:258px" width="95" height="30" viewBox="0 0 95 30"><path d="M2 20Q45 -6 90 16" fill="none" stroke="#bbb" stroke-width="2"/><path d="M82 9l8 7-10 3" fill="none" stroke="#bbb" stroke-width="2"/></svg>
    <svg class="step-arrow" style="left:560px" width="95" height="30" viewBox="0 0 95 30"><path d="M2 20Q45 -6 90 16" fill="none" stroke="#bbb" stroke-width="2"/><path d="M82 9l8 7-10 3" fill="none" stroke="#bbb" stroke-width="2"/></svg>
  </div>

  <div class="divider"><span class="divider-knob"><svg width="12" height="14" viewBox="0 0 12 14"><path d="M6 13V2M1 7l5-5 5 5" fill="none" stroke="#aaa" stroke-width="1.5"/></svg></span></div>

  <h2 class="cta-title">Looking to Rent a Property</h2>
  <p class="cta-sub">which satisfy your Requirements and fits your Budget !</p>
  <a class="btn cta-btn" href="#">CONTACT US</a>
</section>

<footer class="site-footer">
  <nav class="footer-links">
    <a href="#">Home</a><span class="sep">&middot;</span><a href="#">About</a><span class="sep">&middot;</span><a href="#">Privacy Policy</a><span class="sep">&middot;</span><a class="hot" href="#">Tearms &amp; Condition</a><span class="sep">&middot;</span><a href="#">Cookies</a><span class="sep">&middot;</span><a href="#">Contact Us</a>
  </nav>
  <p class="copyright">Copyright by Copperline Properties 2016</p>
  <div class="socials"><span></span><span class="hot"></span><span></span><span></span><span></span></div>
</footer>

</body>
</html>
```